Website header graphic

I'm looking for a professional website header graphic to be designed based on the attached mockup. I'm open to suggestions on the layout. Notes:
1. The text at the bottom should be graphical in some way. Each feature (CRM, etc.) in their individual clouds??? I'll leave it to your creative skills. :)
2. The van needs to have a wrap design that does NOT have a company name, but has the words HVAC, Plumbing, Electrical and look like a real work van.
3. Need to include a 25 year badge. Does not have to be like the one in the mockup. Just added that for reference. Just needs a design that works with the rest of the graphic.
4. I do need the final deliverable in a PSD layered file in 300dpi
5. End result must be realistic clouds, van, etc. with a professional look. Not looking for a cartoon or kids style illustration.
Thank you, Dwight

```html
<!DOCTYPE html>
<html lang="en">
<head>
<meta charset="utf-8">
<title>Cloud Business Software Header</title>
<link href="https://fonts.googleapis.com/css2?family=Montserrat:ital,wght@0,400;0,600;0,700;0,800;1,400;1,500;1,900&family=Anton&display=swap" rel="stylesheet">
<style>
  :root {
    --page: #ffffff;
    --sky-top: #a6e3fa;
    --sky-mid: #c4ecfb;
    --cloud: #f6f9fc;
    --navy: #0c2d8c;
    --red: #e8151f;
    --silver-light: #f2f2f2;
    --silver-dark: #9c9c9c;
    --label: #111111;
    --icon: #1b3ea0;
    --year: #8c8c8c;
  }
  * { margin: 0; padding: 0; box-sizing: border-box; }
  html, body { width: 1200px; height: 612px; overflow: hidden; background: var(--page); }
  .banner {
    position: absolute; left: 0; top: 86px; width: 1200px; height: 440px; overflow: hidden;
    background:
      radial-gradient(ellipse 420px 140px at 300px 440px, var(--cloud) 30%, transparent 75%),
      radial-gradient(ellipse 520px 160px at 950px 450px, var(--cloud) 30%, transparent 75%),
      radial-gradient(ellipse 300px 110px at 620px 330px, rgba(255,255,255,.8) 20%, transparent 75%),
      linear-gradient(180deg, var(--sky-top) 0%, var(--sky-mid) 55%, var(--cloud) 100%);
    font-family: "Montserrat", sans-serif;
  }
  .headline {
    position: absolute; left: 48px; top: 26px;
    font-weight: 900; font-style: italic; font-size: 52px; line-height: 59px;
    color: var(--navy); letter-spacing: -0.5px;
    text-shadow: 2px 2px 0 #fff, -1px -1px 0 #fff, 1px -1px 0 #fff, -1px 1px 0 #fff;
  }
  .tagline {
    position: absolute; left: 48px; top: 213px; width: 430px; height: 37px;
    background: var(--red); transform: skewX(-14deg);
    display: flex; align-items: center; justify-content: center;
  }
  .tagline span {
    transform: skewX(14deg); color: #fff; font-style: italic; font-weight: 500; font-size: 17px;
  }
  .badge-number {
    position: absolute; left: 48px; top: 248px;
    font-weight: 800; font-size: 176px; line-height: 1; letter-spacing: -16px;
    background: linear-gradient(160deg, var(--silver-light) 20%, var(--silver-dark) 60%, #e6e6e6 85%);
    -webkit-background-clip: text; background-clip: text; color: transparent;
    filter: drop-shadow(3px 4px 3px rgba(0,0,0,.25));
  }
  .badge-text {
    position: absolute; left: 257px; top: 308px;
    font-style: italic; font-weight: 400; font-size: 27px; line-height: 33px; color: var(--year);
    padding-bottom: 4px; border-bottom: 2px solid #b5b5b5; width: 140px; white-space: nowrap;
  }
  .van {
    position: absolute; left: 763px; top: 94px; width: 407px; height: 248px;
    background: linear-gradient(170deg, #ffffff 0%, #e9edf0 60%, #8d9399 100%);
    border-radius: 30px 60px 20px 40px;
  }
  .van-wrap {
    position: absolute; left: 1051px; top: 143px; transform: rotate(3deg);
    font-family: "Anton", sans-serif; color: var(--red); font-size: 27px; line-height: 30px; text-align: center;
  }
  .features { position: absolute; left: 0; top: 0; width: 1200px; height: 440px; }
  .label {
    position: absolute; font-weight: 700; font-size: 18px; color: var(--label); white-space: nowrap;
  }
</style>
</head>
<body>
<section class="banner">
  <h1 class="headline">GROW<br>YOUR BUSINESS<br>ON THE CLOUD</h1>
  <div class="tagline"><span>TRUE All-In-One Services Business Software</span></div>

  <div class="badge-number">25</div>
  <div class="badge-text">Year<br>Anniversary</div>

  <div class="van" role="img" aria-label="Photo of a white service work van"></div>
  <div class="van-wrap">HVAC<br>Plumbing<br>Electrical</div>

  <svg class="features" viewBox="0 0 1200 440" aria-hidden="true">
    <defs>
      <filter id="soft" x="-30%" y="-30%" width="160%" height="160%">
        <feDropShadow dx="0" dy="2" stdDeviation="2" flood-color="#000" flood-opacity=".25"/>
      </filter>
    </defs>
    <path d="M863 75 Q905 80 928 110 M781 81 Q830 68 863 75 M715 128 Q745 96 781 81 M683 201 Q690 160 715 128 M694 282 Q676 240 683 201 M745 350 Q708 320 694 282 M830 373 Q785 372 745 350 M830 373 Q900 360 960 320"
      fill="none" stroke="#8aa6c4" stroke-width="1.2" stroke-dasharray="4 4"/>
    <g fill="#fff" stroke="#dce6ef" stroke-width="2" filter="url(#soft)">
      <circle cx="781" cy="81" r="22"/><circle cx="863" cy="75" r="22"/>
      <circle cx="715" cy="128" r="22"/><circle cx="683" cy="201" r="22"/>
      <circle cx="694" cy="282" r="22"/><circle cx="745" cy="350" r="22"/>
      <circle cx="830" cy="373" r="22"/>
    </g>
    <g fill="none" stroke="var(--icon)" stroke-width="1.5" stroke-linecap="round" stroke-linejoin="round">
      <!-- payroll: hand with coin -->
      <circle cx="786" cy="75" r="5"/><path d="M772 90 h6 l8 -5 h6"/><path d="M772 86 v8"/>
      <!-- crm: people loop -->
      <circle cx="863" cy="69" r="3"/><circle cx="855" cy="79" r="3"/><circle cx="871" cy="79" r="3"/>
      <path d="M856 66 a10 10 0 0 1 14 0 M873 85 a10 10 0 0 1 -20 0"/>
      <!-- accounting: calculator -->
      <rect x="706" y="118" width="14" height="18" rx="1.5"/><path d="M709 122 h8 M709 127 h2 M714 127 h2 M709 131 h2 M714 131 h2"/>
      <ellipse cx="724" cy="134" rx="4" ry="2"/>
      <!-- inventory: checklist -->
      <rect x="676" y="191" width="14" height="20" rx="1.5"/><path d="M679 196 h2 M683 196 h5 M679 201 h2 M683 201 h5 M679 206 h2 M683 206 h5"/>
      <!-- marketing: megaphone -->
      <path d="M686 284 l14 -8 v14 z M689 286 l2 6"/><path d="M704 278 l3 -2 M705 283 h3"/>
      <!-- dispatch: document -->
      <path d="M738 339 h10 l5 5 v17 h-15 z"/><path d="M741 350 h9 M741 354 h9 M741 358 h6"/>
      <!-- sales: hand with chart -->
      <path d="M821 382 h6 l8 -5 h5"/><path d="M826 372 l4 -4 3 3 5 -6"/>
    </g>
  </svg>

  <span class="label" style="left:724px; top:30px; width:60px; text-align:center;">Payroll</span>
  <span class="label" style="left:838px; top:24px; width:50px; text-align:center;">CRM</span>
  <span class="label" style="right:510px; top:88px;">Accounting</span>
  <span class="label" style="right:550px; top:192px;">Inventory</span>
  <span class="label" style="left:568px; top:298px; width:100px; text-align:center;">Marketing</span>
  <span class="label" style="left:684px; top:384px; width:80px; text-align:center;">Dispatch</span>
  <span class="label" style="left:800px; top:405px; width:60px; text-align:center;">Sales</span>
</section>
</body>
</html>
```